Lanternwick Home & Commercial Services, Inc.

I need a facebook design for our commercial repair/maintenance company based in Austin, TX. We offer many commercial services:plumbing, HVAC, Carpet/Air duct cleaning, Fire and water restoration, and general maintenance services
Our customer base includes commercial government organizations as NRDX and Camp Tolliver. We serve as the general contractor for these organizations and can handle any scope of work. ie flooring install, drywall, asbestos abatement, and mold removal.
We need a facebook design that communicates to our customer that we strive in customer satisfaction and pricing.
Updates
Logo uploaded. I will also upload photos for some job that have been completed.
I don't have images of our employees actively doing a job. I do have before and after picture that intend to post after fb cover is created.
I like the designs. I will sit with my husband tonight to brainstorm or select a design. Keep submitting, please.

```html
<!DOCTYPE html>
<html lang="en">
<head>
<meta charset="utf-8">
<title>Lanternwick Home &amp; Commercial Services – Cover</title>
<link rel="stylesheet" href="https://fonts.googleapis.com/css2?family=Tinos:wght@400;700&display=swap">
<style>
  :root {
    --bg: #f2f3f1;
    --word-faint: #dcdfd9;
    --word-large: #c9cdc5;
    --word-mid: #c2c7be;
    --word-soft: #cdd1c9;
    --brand: #2d5a29;
    --badge: #2e5f8a;
  }
  html, body {
    margin: 0;
    padding: 0;
    overflow: hidden;
    background: var(--bg);
  }
  .cover {
    display: block;
    width: 1200px;
    height: 444px;
    background: var(--bg);
  }
  .word {
    font-family: "Tinos", "Times New Roman", serif;
    font-weight: 400;
  }
  .word--faint { fill: var(--word-faint); }
  .word--large { fill: var(--word-large); }
  .word--mid { fill: var(--word-mid); }
  .word--soft { fill: var(--word-soft); }
  .bullet { fill: var(--word-mid); }
  .brand-name {
    font-family: "Tinos", "Times New Roman", serif;
    font-weight: 700;
    fill: var(--brand);
  }
  .listing-badge { fill: var(--badge); }
</style>
</head>
<body>
<svg class="cover" width="1200" height="444" viewBox="0 0 1200 444" xmlns="http://www.w3.org/2000/svg">
  <g class="word-cloud">
    <text class="word word--faint" x="0" y="148" font-size="215" textLength="472" lengthAdjust="spacingAndGlyphs">repair</text>
    <text class="word word--soft" x="705" y="24" font-size="44" textLength="262" lengthAdjust="spacingAndGlyphs">maintenance</text>
    <text class="word word--mid" x="455" y="87" font-size="54" textLength="202" lengthAdjust="spacingAndGlyphs">plumbing</text>
    <text class="word word--large" x="681" y="102" font-size="112" textLength="456" lengthAdjust="spacingAndGlyphs">guaranteed</text>
    <text class="word word--mid" x="226" y="183" font-size="54" textLength="56" lengthAdjust="spacingAndGlyphs">air</text>
    <text class="word word--mid" x="494" y="158" font-size="54" textLength="169" lengthAdjust="spacingAndGlyphs">cleaning</text>
    <text class="word word--mid" x="743" y="165" font-size="54" textLength="107" lengthAdjust="spacingAndGlyphs">mold</text>
    <circle class="bullet" cx="931" cy="134" r="12"/>
    <text class="word word--mid" x="966" y="172" font-size="54" textLength="113" lengthAdjust="spacingAndGlyphs">ducts</text>
    <text class="word word--mid" x="296" y="209" font-size="54" textLength="162" lengthAdjust="spacingAndGlyphs">flooring</text>
    <text class="word word--soft" x="179" y="261" font-size="50" textLength="171" lengthAdjust="spacingAndGlyphs">asbestos</text>
    <text class="word word--soft" x="413" y="303" font-size="54" textLength="135" lengthAdjust="spacingAndGlyphs">HVAC</text>
    <text class="word word--large" x="575" y="282" font-size="185" textLength="620" lengthAdjust="spacingAndGlyphs">services</text>
    <text class="word word--mid" x="630" y="370" font-size="54" textLength="260" lengthAdjust="spacingAndGlyphs">construction</text>
  </g>
  <g class="brand">
    <text class="brand-name" x="296" y="394" font-size="40" textLength="284" lengthAdjust="spacingAndGlyphs">LANTERNWICK</text>
    <text class="brand-name" x="298" y="424" font-size="17" textLength="284" lengthAdjust="spacingAndGlyphs">HOME &amp; COMMERCIAL SERVICES</text>
  </g>
  <rect class="listing-badge" x="608" y="380" width="32" height="50" rx="3"/>
</svg>
</body>
</html>
```